Colorful logo using law firm name. letterhead Quillon Law national consumer fraud.

We only bring consumer fraud litigation against fortune 50 companies across the United States

Reason: I want 1 day extension not 5. Being new at this, I want my letterhead to match everything else. Sorry for creating confusion.

Please review all my updates and pictures. If someone knows how to tell me I can get the webpage done. Change: 4 offiecs: Cal, NC, AL, and MS. I have numbers for each for website except MS. I want pictures, many I have uploaded. Need office picttures, Downtown SF, etc. I have provided info for my the "about the firm" (mostly me), investigations, and representative cases. The main page should be be big city perferably SF, whcih I sent picture. Also, inside and out of offices that I have uploaded. On website, I hope to list the addres and phone number for each locatiom. Thank you for yoru patience.

Law Firm

```html
<!DOCTYPE html>
<html lang="en">
<head>
<meta charset="utf-8">
<title>Quillon Law P.C. — Letterhead</title>
<link rel="stylesheet" href="https://fonts.googleapis.com/css2?family=Cinzel:wght@400;600;700&display=swap">
<style>
  :root {
    --navy: #1b2e4b;
    --gold: #a8865a;
    --paper: #ffffff;
    --page-edge: #d6d6d6;
    --mark: #f1f1f1;
    --ink-light: #ffffff;
  }
  * { box-sizing: border-box; margin: 0; padding: 0; }
  html, body {
    width: 1200px; height: 847px; overflow: hidden;
    background: #ffffff;
    font-family: "Cinzel", Georgia, serif;
  }
  .canvas { position: relative; width: 1200px; height: 847px; }

  .letterhead {
    position: absolute; left: 306px; top: 15px;
    width: 580px; height: 821px;
    background: var(--paper);
    border: 1px solid var(--page-edge);
    overflow: hidden;
  }

  .firm-name {
    position: absolute; left: 0; right: 0; top: 52px;
    text-align: center;
    color: var(--navy);
    font-weight: 600;
    font-size: 36px;
    letter-spacing: 1px;
  }
  .firm-site {
    position: absolute; left: 0; right: 0; top: 122px;
    text-align: center;
    color: var(--navy);
    font-weight: 600;
    font-size: 15px;
    letter-spacing: 0.3px;
  }

  .practice-band {
    position: absolute; left: 0; right: 0; top: 157px; height: 32px;
    background: var(--gold);
    color: var(--ink-light);
    font-weight: 700;
    font-size: 19px;
    line-height: 32px;
    text-align: center;
    letter-spacing: 0.3px;
  }

  .background-name {
    position: absolute; left: -40px; top: 430px;
    width: 760px;
    transform: rotate(-52deg);
    transform-origin: center;
    color: var(--mark);
    font-weight: 400;
    font-size: 118px;
    white-space: nowrap;
    text-align: center;
    letter-spacing: 4px;
  }

  .office-band {
    position: absolute; left: 0; right: 0; top: 731px; height: 24px;
    background: var(--gold);
  }
  .office-details {
    position: absolute; left: 0; right: 0; top: 755px; bottom: 0;
    background: var(--navy);
  }
  .office {
    position: absolute; top: 731px;
    color: var(--ink-light);
  }
  .office-state {
    height: 24px; line-height: 24px;
    font-size: 13px; font-weight: 700; letter-spacing: 0.4px;
  }
  .office-address {
    margin-top: 10px;
    font-size: 7px; font-weight: 600; line-height: 9px;
  }
  .office-phone {
    margin-top: 13px;
    font-size: 9px; font-weight: 600;
  }
  .office--ca { left: 18px; text-align: left; }
  .office--nc { left: 150px; width: 140px; text-align: center; }
  .office--ms { left: 300px; width: 130px; text-align: center; }
  .office--al { right: 18px; text-align: right; }
</style>
</head>
<body>
<div class="canvas">
  <main class="letterhead">
    <div class="background-name" aria-hidden="true">QUILLON LAW</div>

    <header>
      <div class="firm-name">QUILLON LAW P.C.</div>
      <div class="firm-site">www.QUILLONLAWPC.com</div>
    </header>

    <div class="practice-band">CONSUMER CLASS AND COMPLEX LITIGATION</div>

    <footer>
      <div class="office-band"></div>
      <div class="office-details"></div>

      <div class="office office--ca">
        <div class="office-state">California</div>
        <div class="office-address">318 Harbor Street Suite 210<br>San Francisco, CA 94111</div>
        <div class="office-phone">Tel: 415-555-0142</div>
      </div>
      <div class="office office--nc">
        <div class="office-state">North Carolina</div>
        <div class="office-address">4120 Maple Ridge Road, 4th Floor<br>Charlotte, NC 28210</div>
        <div class="office-phone">Tel: 704-555-0187</div>
      </div>
      <div class="office office--ms">
        <div class="office-state">Mississippi</div>
        <div class="office-address">address line 1<br>address line 2, zip code</div>
        <div class="office-phone">Tel: 000-000-0000</div>
      </div>
      <div class="office office--al">
        <div class="office-state">Alabama</div>
        <div class="office-address">905 Elm Avenue S. Suite 118<br>Birmingham, AL 35205</div>
        <div class="office-phone">Tel: 205-555-0163</div>
      </div>
    </footer>
  </main>
</div>
</body>
</html>
```